Business Card Design Project

I am a new business offering a consulting service in Homeware buying, product development and trend forecasting. I would like to use colours that are current and on trend now. Needs to be eye catching, speak of creativity and design.

Front: Matt charcoal card with black gloss embossing name print
Back: white with Pink text

Pink pantone: 812c

Target Market(s)

Retailers and Wholesalers of Homeware products

Industry/Entity Type

Business

Requirements
Must have
• Please go to this link and the card on this link is what I am looking for.

http://www.foliorama.net/gallery/Blank_sheet-KX/402817

1. Card Front

Name on front of card: MARGOT FINCHLEY

2. Back card

The following text must be designed onto the card:

Address: 17 Walloway Street ,Paddington, 2021, NSW, Sydney, Australia
Mobile: +61 (0)412305718
Email: finchmel@wirrolink.net.au

Homeware trends
Product development and sourcing
Strategic Buying management
Nice to have
• Creativity in selection of font, composition and proportion.
Should not have
• I don't want to see graphics/shapes on the card.

```html
<!DOCTYPE html>
<html lang="en">
<head>
<meta charset="utf-8">
<title>Margot Finchley — Business Card Front</title>
<link rel="stylesheet" href="https://fonts.googleapis.com/css2?family=Montserrat:wght@500&display=swap">
<style>
  :root {
    --charcoal: #171a1b;
    --gloss-black: #000000;
    --pantone-pink: #e817d8;
  }
  html, body {
    margin: 0;
    padding: 0;
    width: 1200px;
    height: 699px;
    overflow: hidden;
    background: var(--charcoal);
  }
  .card-front {
    display: block;
    width: 1200px;
    height: 699px;
  }
  .trim-frame {
    fill: none;
    stroke: var(--pantone-pink);
    stroke-width: 3.5;
  }
  .safe-frame {
    fill: none;
    stroke: var(--pantone-pink);
    stroke-width: 3.5;
    stroke-dasharray: 32 20;
  }
  .name-line {
    font-family: "Montserrat", "Helvetica Neue", Arial, sans-serif;
    font-weight: 500;
    font-size: 100px;
    fill: var(--gloss-black);
  }
</style>
</head>
<body>
  <svg class="card-front" viewBox="0 0 1200 699" xmlns="http://www.w3.org/2000/svg">
    <rect class="trim-frame" x="37" y="37" width="1126" height="624"/>
    <rect class="safe-frame" x="74" y="74" width="1051" height="550"/>
    <text class="name-line" x="600" y="386" text-anchor="middle"
          textLength="940" lengthAdjust="spacing">Margot Finchley</text>
  </svg>
</body>
</html>
```